Save the date for wedding

A save the date for our wedding. We're looking for a simple and sleek invite. I would prefer not alot of calligraphy. Minimalism is good. The basic info to include is as follows:
Names: Mona and Felix
Date: June 9th
Where: Ottawa, Ontario
In small print please include that there will be a reception in Edmonton AB September 1st for those who cannot make it to Ottawa.
Please see the attached file for a style idea. Doesn’t have to be exactly like that, but something like that.

```html
<!DOCTYPE html>
<html lang="en">
<head>
<meta charset="utf-8">
<title>Save the Date – Mona and Felix</title>
<link rel="stylesheet" href="https://fonts.googleapis.com/css2?family=Antonio:wght@300;500&family=Jost:ital,wght@0,300;0,400;0,600;1,200&display=swap">
<style>
  :root {
    --plum: #5a1f63;
    --mauve: #8a6c91;
    --sand: #c9aa92;
    --sand-deep: #b48e74;
    --paper: #fbfaf8;
  }
  * { margin: 0; padding: 0; box-sizing: border-box; }
  html, body { width: 1200px; height: 1200px; overflow: hidden; background: var(--paper); }
  .card { position: relative; width: 1200px; height: 1200px; background: var(--paper); overflow: hidden; }
  .side-pattern {
    position: absolute; top: 0; height: 1200px;
    background: radial-gradient(ellipse at 40% 50%, #efe6de 0%, var(--sand) 45%, var(--sand-deep) 100%);
  }
  .side-pattern--left { left: 0; width: 274px; }
  .side-pattern--right { right: 0; width: 259px; }
  .centre-panel { position: absolute; left: 274px; width: 667px; top: 0; height: 1200px; background: var(--paper); }
  .flourish {
    position: absolute; left: 50%; transform: translateX(-50%);
    width: 210px; height: 72px; background: linear-gradient(90deg, #a37aa8, var(--plum), #a37aa8);
    border-radius: 36px; opacity: .85;
  }
  .flourish--top { top: -16px; }
  .flourish--bottom { bottom: -16px; }
  .text { position: absolute; left: 274px; width: 667px; text-align: center; white-space: nowrap; }
  .tagline {
    top: 152px; font-family: "Antonio", sans-serif; font-weight: 300;
    font-size: 46px; line-height: 42px; letter-spacing: 2px; color: var(--mauve);
  }
  .name {
    font-family: "Antonio", sans-serif; font-weight: 500; color: var(--plum);
    font-size: 205px; line-height: 205px; letter-spacing: -1px;
  }
  .name--first { top: 320px; }
  .name--second { top: 542px; }
  .conjunction {
    top: 534px; font-family: "Jost", sans-serif; font-weight: 300;
    font-size: 28px; line-height: 28px; letter-spacing: 4px; color: var(--plum);
  }
  .date { top: 868px; font-family: "Jost", sans-serif; font-size: 100px; line-height: 100px; color: var(--plum); }
  .date__num { font-style: italic; font-weight: 200; }
  .date__month { font-weight: 600; }
  .venue {
    top: 990px; font-family: "Jost", sans-serif; font-weight: 400;
    font-size: 30px; line-height: 30px; letter-spacing: 6px; color: var(--plum);
  }
  .small-print {
    top: 1048px; font-family: "Jost", sans-serif; font-weight: 300;
    font-size: 19px; line-height: 27px; color: var(--mauve);
  }
</style>
</head>
<body>
  <div class="card">
    <div class="side-pattern side-pattern--left" role="img" aria-label="Sand-coloured baroque damask pattern with white scrolls"></div>
    <div class="side-pattern side-pattern--right" role="img" aria-label="Sand-coloured baroque damask pattern with white scrolls"></div>
    <div class="centre-panel">
      <div class="flourish flourish--top" role="img" aria-label="Plum baroque flourish ornament"></div>
      <div class="flourish flourish--bottom" role="img" aria-label="Plum baroque flourish ornament"></div>
    </div>
    <p class="text tagline">The best time for new beginnings<br>is now</p>
    <h1 class="text name name--first">Mona</h1>
    <p class="text conjunction">-AND-</p>
    <h1 class="text name name--second">Felix</h1>
    <p class="text date"><span class="date__num">9</span> <span class="date__month">June</span></p>
    <p class="text venue">OTTAWA, ONTARIO</p>
    <p class="text small-print">Can't make it to Ottawa? Join us for a reception<br>in Edmonton, AB on September 1st</p>
  </div>
</body>
</html>
```